Wills & Estate Planning *

I have my own logo, just looking for a nice eye catching background with good quality.

Could we find a place for 'We give you the peace of mind you deserve'
Updates

Could we find somewhere on the card to put 'We give you the peace of mind you deserve' Thanks.

Target Market(s)

40+ age

Industry/Entity Type

Law Firm

Contact Information for Business Card

Colin Maranby
01632 960581
admin@oakmerelegacy.co.uk
www.oakmerelegacy.co.uk

Requirements
Must have
• Please use my logo attached on the brief

```html
<!DOCTYPE html>
<html lang="en">
<head>
<meta charset="utf-8">
<title>Oakmere Legacy – Business Card</title>
<link rel="stylesheet" href="https://fonts.googleapis.com/css2?family=Arimo:wght@400;700&display=swap">
<style>
  :root {
    --backdrop: #2b2b2d;
    --card-white: #ffffff;
    --card-mist: #e9eaee;
    --navy: #243a74;
    --navy-deep: #1c2f60;
    --slate: #6f7386;
    --rule-grey: #8e92a3;
    --pale-text: #c9cfe0;
    --faint-navy: #b9c1d4;
  }
  * { box-sizing: border-box; margin: 0; padding: 0; }
  html, body {
    width: 1200px; height: 997px; overflow: hidden;
    background: var(--backdrop);
    font-family: "Arimo", Arial, sans-serif;
  }
  .stage { position: relative; width: 1200px; height: 997px; }
  .card {
    position: absolute; left: 285px; width: 630px; height: 360px;
    border-radius: 18px; overflow: hidden;
    box-shadow: 0 10px 30px rgba(0,0,0,.45);
  }

  /* Back of the card */
  .card--back {
    top: 98px;
    padding: 0 40px;
    background: linear-gradient(160deg, var(--card-white) 0%, var(--card-mist) 100%);
    display: flex; flex-direction: column; align-items: center; justify-content: center;
    gap: 18px;
  }
  .card--back .brand-name {
    font-size: 46px; font-weight: 400; letter-spacing: 3px; white-space: nowrap;
    color: var(--faint-navy); text-transform: uppercase;
  }
  .card--back .tagline {
    font-size: 17px; color: var(--slate); letter-spacing: .5px; white-space: nowrap;
  }

  /* Front of the card */
  .card--front { top: 518px; background: var(--card-white); }
  .front-header {
    position: absolute; top: 0; left: 0; right: 0; height: 172px;
    background: linear-gradient(180deg, var(--card-white) 0%, #f1f2f5 100%);
    display: flex; flex-direction: column; align-items: center; justify-content: center;
    gap: 10px;
  }
  .front-header .brand-name {
    font-size: 40px; font-weight: 400; letter-spacing: 3px; white-space: nowrap;
    color: var(--navy); text-transform: uppercase;
  }
  .front-header .tagline {
    font-size: 14px; color: var(--slate); letter-spacing: 1px; white-space: nowrap;
  }
  .header-rule {
    position: absolute; top: 176px; left: 0; right: 0; height: 5px;
    background: var(--rule-grey);
  }
  .contact-band {
    position: absolute; top: 186px; left: 0; right: 0; height: 158px;
    background: linear-gradient(180deg, var(--navy) 0%, var(--navy-deep) 100%);
  }
  .band-notch { position: absolute; top: 180px; left: 52px; width: 26px; height: 12px; }
  .foot-strip {
    position: absolute; bottom: 0; left: 0; right: 0; height: 16px;
    background: var(--card-mist);
  }
  .person { position: absolute; left: 44px; top: 20px; color: var(--card-white); }
  .person-name {
    font-size: 21px; font-weight: 700; letter-spacing: .5px; text-transform: uppercase;
  }
  .person-role { font-size: 15px; color: var(--pale-text); margin-top: 3px; }
  .contact-list {
    position: absolute; left: 44px; top: 84px; list-style: none;
    color: var(--pale-text); font-size: 16px;
  }
  .contact-list li { display: flex; align-items: center; gap: 10px; margin-bottom: 10px; }
  .contact-icon { width: 20px; height: 20px; flex: none; }
  .web-address {
    position: absolute; right: 30px; top: 22px;
    color: var(--card-white); font-size: 17px; font-weight: 700;
  }
</style>
</head>
<body>
<main class="stage">

  <section class="card card--back" aria-label="Card back">
    <span class="brand-name">Oakmere Legacy</span>
    <p class="tagline">We give you the peace of mind you deserve</p>
  </section>

  <section class="card card--front" aria-label="Card front">
    <header class="front-header">
      <span class="brand-name">Oakmere Legacy</span>
      <p class="tagline">We give you the peace of mind you deserve</p>
    </header>
    <div class="header-rule"></div>
    <div class="contact-band">
      <div class="person">
        <p class="person-name">Colin Maranby</p>
        <p class="person-role">Managing Director</p>
      </div>
      <ul class="contact-list">
        <li>
          <svg class="contact-icon" viewBox="0 0 20 20" aria-hidden="true">
            <circle cx="10" cy="10" r="10" fill="#c9cfe0"/>
            <path d="M6.5 5.5l2 0 1 2.5-1.3 1c.6 1.3 1.5 2.2 2.8 2.8l1-1.3 2.5 1v2c0 .6-.5 1-1 1C9 14.2 5.8 11 5.5 6.5c0-.6.4-1 1-1z" fill="#243a74"/>
          </svg>
          <span>01632 960581</span>
        </li>
        <li>
          <svg class="contact-icon" viewBox="0 0 20 20" aria-hidden="true">
            <circle cx="10" cy="10" r="10" fill="#c9cfe0"/>
            <rect x="5" y="6.5" width="10" height="7" rx="1" fill="#243a74"/>
            <path d="M5.5 7l4.5 3.5L14.5 7" stroke="#c9cfe0" stroke-width="1" fill="none"/>
          </svg>
          <span>admin@oakmerelegacy.co.uk</span>
        </li>
      </ul>
      <p class="web-address">www.oakmerelegacy.co.uk</p>
    </div>
    <svg class="band-notch" viewBox="0 0 26 12" aria-hidden="true">
      <polygon points="0,12 13,0 26,12" fill="#243a74"/>
    </svg>
    <div class="foot-strip"></div>
  </section>

</main>
</body>
</html>
```